Use responsive design to make this page look and behave awesome in any size

YOU CAN SUBMIT PSD, HOWEVER, THE WINNER MUST SUBMIT PROVIDE A SINGLE CODED PAGE PER THE LINK AND INSTRUCTIONS AT THE BOTTOM OF THIS BRIEF. While developing an internal website, we realized we are not super great at making things look awesome and responsive for phone/tablet/desktop. Thats where you come in. We want you to take this code, Fork it, and then make it look awesome and work great on any size device.

Task at hand:

This page is a simple dashboard showing how a number of stores stack up against each other and against a corporate goal.

Top: Goal title, and where the logged in person's store stands in the ranking.
Green means you are in compliance
Red means you are not in compliance

Middle: Description of goal. Words to describe what the corporate goal is, and a target number.

Bottom: Here we just want to show the top 10 and bottom 5 out of 100+ stores. if your in the top ten, you are highlighted. If your in the bottom 5, you will be highlighted there too. If you are in the middle, we would put the your store info between the top and bottom... indicating your in the middle.
Green means you they are in compliance
Red means they are not in compliance

Your Mission is not only to make this look fantastic and responsive, but to have usable code in there.

You don't need to do any logic. All we care about is look and feel and responsive behavior on different size browsers.

The winner obviously gets the prize, and hopefully can become a solid resource to do more of this type of thing for us in the future.

Instructions:
Go to this link: https://codewharf.example/edit/tpl-tallyboard-widget
Click on the blue Fork button. This will give you a new URL that you can paste back into the contest to review results for us to see your work.
Uploading pictures is not necessary as the responsive code is what is important here.

Good luck!

Number of Pages Required

1 page

Requirements
Must have
• The page must be responsive and look very professional AND game like.
Should not have
• plugins. just native code

```html
<!DOCTYPE html>
<html lang="en">
<head>
<meta charset="utf-8">
<title>Lead Measures</title>
<link href="https://fonts.googleapis.com/css2?family=Michroma&family=Poppins:wght@400;500&display=swap" rel="stylesheet">
<style>
:root{
  --bg-top:#2a2a2a;
  --bg-bottom:#050505;
  --card-bg:#121212;
  --frame:#aebcbe;
  --accent:#35d4f0;
  --band:#0b0b6b;
  --white:#ffffff;
  --green:#35c435;
  --red:#e0262c;
  --highlight:#a01c1c;
  --icon-bg:#0f5560;
}
*{box-sizing:border-box;margin:0;padding:0}
html,body{width:1200px;height:960px;overflow:hidden}
body{
  background:radial-gradient(ellipse at 50% 20%,var(--bg-top),var(--bg-bottom) 80%);
  font-family:"Poppins",sans-serif;color:var(--white);position:relative;
}
.page-title{
  position:absolute;top:80px;left:0;width:1200px;text-align:center;
  font-family:"Michroma",sans-serif;font-size:30px;letter-spacing:1px;font-weight:400;
}
.board{position:absolute;top:194px;left:38px;display:flex;gap:28px}
.card{
  position:relative;width:260px;height:680px;background:var(--card-bg);
  border:2px solid var(--frame);
  clip-path:polygon(18px 0,100% 0,100% calc(100% - 18px),calc(100% - 18px) 100%,0 100%,0 18px);
}
.card-frame{position:absolute;inset:-2px;width:264px;height:684px;pointer-events:none}
.card-head{height:94px;display:flex;align-items:center;padding-left:14px;gap:14px}
.card-icon{
  width:57px;height:57px;border-radius:6px;
  background:radial-gradient(circle,#1a7b88,var(--icon-bg));
  display:flex;align-items:center;justify-content:center;
}
.card-title{font-family:"Michroma",sans-serif;font-size:20px}
.card-score{font-family:"Michroma",sans-serif;font-size:20px;color:var(--green);margin-left:8px}
.goal{
  height:133px;background:var(--band);text-align:center;
  display:flex;flex-direction:column;justify-content:center;align-items:center;padding:0 10px;
}
.goal-text{font-family:"Michroma",sans-serif;font-size:13px;line-height:16px}
.goal-target{font-family:"Michroma",sans-serif;font-size:28px;color:var(--accent);margin-top:16px}
.ranks{list-style:none;margin-top:3px}
.ranks.bottom{margin-top:28px}
.rank{
  display:grid;grid-template-columns:38px 1fr 46px;align-items:center;
  height:26.8px;padding:0 20px 0 18px;font-size:14px;
}
.rank .pos{color:var(--white)}
.rank .val{text-align:right}
.ok{color:var(--green)}
.bad{color:var(--red)}
.rank.mine{background:var(--highlight)}
.rank.mine .name,.rank.mine .val{color:var(--white)}
</style>
</head>
<body>
<h1 class="page-title">LEAD MEASURES</h1>
<main class="board">

<section class="card">
  <svg class="card-frame" viewBox="0 0 264 684"><path d="M2 60 V20 L20 2 H100" fill="none" stroke="#4fb7c4" stroke-width="3"/><path d="M262 620 V664 L244 682 H160" fill="none" stroke="#4fb7c4" stroke-width="3"/></svg>
  <header class="card-head">
    <div class="card-icon"><svg width="34" height="30" viewBox="0 0 34 30"><g fill="var(--accent)"><circle cx="8" cy="6" r="3.5"/><circle cx="17" cy="4" r="3.5"/><circle cx="26" cy="6" r="3.5"/><path d="M3 16 q5-7 10 0 q4-7 8 0 q4-7 10 0 v3 H3z"/></g><path d="M3 27 L13 21 L19 24 L31 15" stroke="var(--accent)" stroke-width="3" fill="none"/></svg></div>
    <span class="card-title">Team</span><span class="card-score">92.1%</span>
  </header>
  <div class="goal"><p class="goal-text">Use slow stock whenever possible</p><p class="goal-target">80%</p></div>
  <ol class="ranks">
    <li class="rank"><span class="pos">1</span><span class="name bad">(1) yjcQbtCyQu</span><span class="val bad">1%</span></li>
    <li class="rank"><span class="pos">2</span><span class="name bad">(1) crsmicfXwS</span><span class="val bad">1%</span></li>
    <li class="rank"><span class="pos">3</span><span class="name bad">(2) wnLJojLRSf</span><span class="val bad">2%</span></li>
    <li class="rank"><span class="pos">4</span><span class="name bad">(2) swEbjeRrpi</span><span class="val bad">2%</span></li>
    <li class="rank"><span class="pos">5</span><span class="name bad">(4) oUauMPncOA</span><span class="val bad">4%</span></li>
    <li class="rank"><span class="pos">6</span><span class="name bad">(5) vYuFdHZExR</span><span class="val bad">5%</span></li>
    <li class="rank"><span class="pos">7</span><span class="name bad">(5) jvBnNaGkeE</span><span class="val bad">5%</span></li>
    <li class="rank"><span class="pos">8</span><span class="name bad">(6) CuWllvexCs</span><span class="val bad">6%</span></li>
    <li class="rank"><span class="pos">9</span><span class="name bad">(7) XQFCUbSoko</span><span class="val bad">7%</span></li>
    <li class="rank"><span class="pos">10</span><span class="name bad">(7) GucpFDVVJP</span><span class="val bad">7%</span></li>
  </ol>
  <ol class="ranks bottom">
    <li class="rank"><span class="pos">96</span><span class="name ok">(94) VaDGNkvwai</span><span class="val ok">94%</span></li>
    <li class="rank"><span class="pos">97</span><span class="name ok">(94) IBjPTiBSIh</span><span class="val ok">94%</span></li>
    <li class="rank"><span class="pos">98</span><span class="name ok">(96) iWwFhTvkZb</span><span class="val ok">96%</span></li>
    <li class="rank"><span class="pos">99</span><span class="name ok">(96) IzLClRKlLu</span><span class="val ok">96%</span></li>
    <li class="rank"><span class="pos">100</span><span class="name ok">(96) pXPrzpcrUY</span><span class="val ok">96%</span></li>
  </ol>
</section>

<section class="card">
  <svg class="card-frame" viewBox="0 0 264 684"><path d="M2 60 V20 L20 2 H100" fill="none" stroke="#4fb7c4" stroke-width="3"/><path d="M262 620 V664 L244 682 H160" fill="none" stroke="#4fb7c4" stroke-width="3"/></svg>
  <header class="card-head">
    <div class="card-icon"><svg width="34" height="34" viewBox="0 0 34 34"><circle cx="17" cy="17" r="14" fill="none" stroke="var(--accent)" stroke-width="3"/><circle cx="17" cy="17" r="8" fill="none" stroke="var(--accent)" stroke-width="2"/><path d="M17 17 L11 9" stroke="var(--accent)" stroke-width="3"/></svg></div>
    <span class="card-title">Slow</span><span class="card-score">0%</span>
  </header>
  <div class="goal"><p class="goal-text">Less than 0% of inventory slower than 100 days</p><p class="goal-target">&lt; 1%</p></div>
  <ol class="ranks">
    <li class="rank"><span class="pos">1</span><span class="name ok">(89) NZBGVuImnc</span><span class="val ok">0%</span></li>
    <li class="rank"><span class="pos">2</span><span class="name ok">(80) GaccDehKUO</span><span class="val ok">0%</span></li>
    <li class="rank"><span class="pos">3</span><span class="name ok">(55) aPfpNcqcDh</span><span class="val ok">0%</span></li>
    <li class="rank"><span class="pos">4</span><span class="name ok">(97) YqyVfKlTIl</span><span class="val ok">0%</span></li>
    <li class="rank"><span class="pos">5</span><span class="name ok">(67) PvQdqyeaHr</span><span class="val ok">0%</span></li>
    <li class="rank mine"><span class="pos">6</span><span class="name">(00) Your Store</span><span class="val">2%</span></li>
    <li class="rank"><span class="pos">7</span><span class="name bad">(40) jyMfVYIVbl</span><span class="val bad">2%</span></li>
    <li class="rank"><span class="pos">8</span><span class="name bad">(11) QSESmpDJqw</span><span class="val bad">2%</span></li>
    <li class="rank"><span class="pos">9</span><span class="name bad">(71) nIlaXFpJWv</span><span class="val bad">2%</span></li>
    <li class="rank"><span class="pos">10</span><span class="name bad">(51) ENrkkveKpb</span><span class="val bad">2%</span></li>
  </ol>
  <ol class="ranks bottom">
    <li class="rank"><span class="pos">96</span><span class="name bad">(90) VZgTUWgJTU</span><span class="val bad">8%</span></li>
    <li class="rank"><span class="pos">97</span><span class="name bad">(67) nRGVsKcZhP</span><span class="val bad">9%</span></li>
    <li class="rank"><span class="pos">98</span><span class="name bad">(32) JckeFPUVJV</span><span class="val bad">9%</span></li>
    <li class="rank"><span class="pos">99</span><span class="name bad">(57) RxygcFNCRC</span><span class="val bad">9%</span></li>
    <li class="rank"><span class="pos">100</span><span class="name bad">(20) MmydxeaOMu</span><span class="val bad">10%</span></li>
  </ol>
</section>

<section class="card">
  <svg class="card-frame" viewBox="0 0 264 684"><path d="M2 60 V20 L20 2 H100" fill="none" stroke="#4fb7c4" stroke-width="3"/><path d="M262 620 V664 L244 682 H160" fill="none" stroke="#4fb7c4" stroke-width="3"/></svg>
  <header class="card-head">
    <div class="card-icon"><svg width="34" height="34" viewBox="0 0 34 34"><path d="M6 17 A11 11 0 0 1 26 10 M28 17 A11 11 0 0 1 8 24" fill="none" stroke="var(--accent)" stroke-width="3"/><path d="M26 4 V11 H19 M8 30 V23 H15" fill="none" stroke="var(--accent)" stroke-width="3"/><rect x="12" y="12" width="10" height="10" rx="2" fill="none" stroke="var(--accent)" stroke-width="2"/></svg></div>
    <span class="card-title">Turns</span><span class="card-score">2.2</span>
  </header>
  <div class="goal"><p class="goal-text">Turn inventory 6 or more times a year</p><p class="goal-target">&gt; 6</p></div>
  <ol class="ranks">
    <li class="rank"><span class="pos">1</span><span class="name bad">(8) VZaEOSVkef</span><span class="val bad">0.2</span></li>
    <li class="rank"><span class="pos">2</span><span class="name bad">(3) PcVKNpUNmj</span><span class="val bad">0.2</span></li>
    <li class="rank"><span class="pos">3</span><span class="name bad">(4) RIlyRZsTIn</span><span class="val bad">0.4</span></li>
    <li class="rank"><span class="pos">4</span><span class="name bad">(9) epiNQFtERO</span><span class="val bad">0.6</span></li>
    <li class="rank"><span class="pos">5</span><span class="name bad">(3) FbFOzkjSpF</span><span class="val bad">0.7</span></li>
    <li class="rank"><span class="pos">6</span><span class="name bad">(7) RdzzkcVqtC</span><span class="val bad">0.8</span></li>
    <li class="rank"><span class="pos">7</span><span class="name bad">(1) DiilXiGkTx</span><span class="val bad">0.8</span></li>
    <li class="rank"><span class="pos">8</span><span class="name bad">(1) jxWbwORyVa</span><span class="val bad">0.8</span></li>
    <li class="rank"><span class="pos">9</span><span class="name bad">(4) UyzYfiIMzU</span><span class="val bad">0.8</span></li>
    <li class="rank"><span class="pos">10</span><span class="name bad">(4) KVlgJQBgAc</span><span class="val bad">1</span></li>
  </ol>
  <ol class="ranks bottom">
    <li class="rank"><span class="pos">96</span><span class="name ok">(5) gBeGhPqZNF</span><span class="val ok">9.7</span></li>
    <li class="rank"><span class="pos">97</span><span class="name ok">(8) gGhhZFlCHP</span><span class="val ok">9.7</span></li>
    <li class="rank"><span class="pos">98</span><span class="name ok">(9) emavLKfhzN</span><span class="val ok">9.8</span></li>
    <li class="rank"><span class="pos">99</span><span class="name ok">(7) PyuviZHBxH</span><span class="val ok">9.8</span></li>
    <li class="rank"><span class="pos">100</span><span class="name ok">(5) LIdsyctcWm</span><span class="val ok">9.9</span></li>
  </ol>
</section>

<section class="card">
  <svg class="card-frame" viewBox="0 0 264 684"><path d="M2 60 V20 L20 2 H100" fill="none" stroke="#4fb7c4" stroke-width="3"/><path d="M262 620 V664 L244 682 H160" fill="none" stroke="#4fb7c4" stroke-width="3"/></svg>
  <header class="card-head">
    <div class="card-icon"><svg width="34" height="34" viewBox="0 0 34 34"><path d="M18 5 H29 V16 L15 30 L4 19 Z" fill="none" stroke="var(--accent)" stroke-width="3" stroke-linejoin="round"/><circle cx="23" cy="11" r="2.5" fill="var(--accent)"/></svg></div>
    <span class="card-title">Values</span><span class="card-score">1.9</span>
  </header>
  <div class="goal"><p class="goal-text">Inventory Value to be around 1.25 x you last months INVENTORY sales</p><p class="goal-target">1.25</p></div>
  <ol class="ranks">
    <li class="rank"><span class="pos">1</span><span class="name ok">(8) VZaEOSVkef</span><span class="val ok">0.2</span></li>
    <li class="rank"><span class="pos">2</span><span class="name ok">(3) PcVKNpUNmj</span><span class="val ok">0.2</span></li>
    <li class="rank"><span class="pos">3</span><span class="name ok">(4) RIlyRZsTIn</span><span class="val ok">0.4</span></li>
    <li class="rank"><span class="pos">4</span><span class="name ok">(9) epiNQFtERO</span><span class="val ok">0.6</span></li>
    <li class="rank"><span class="pos">5</span><span class="name ok">(3) FbFOzkjSpF</span><span class="val ok">0.7</span></li>
    <li class="rank"><span class="pos">6</span><span class="name ok">(7) RdzzkcVqtC</span><span class="val ok">0.8</span></li>
    <li class="rank"><span class="pos">7</span><span class="name ok">(1) DiilXiGkTx</span><span class="val ok">0.8</span></li>
    <li class="rank"><span class="pos">8</span><span class="name ok">(1) jxWbwORyVa</span><span class="val ok">0.8</span></li>
    <li class="rank"><span class="pos">9</span><span class="name ok">(4) UyzYfiIMzU</span><span class="val ok">0.8</span></li>
    <li class="rank"><span class="pos">10</span><span class="name ok">(7) SCXuIMdjcB</span><span class="val ok">1</span></li>
  </ol>
  <ol class="ranks bottom">
    <li class="rank"><span class="pos">96</span><span class="name bad">(5) gBeGhPqZNF</span><span class="val bad">9.7</span></li>
    <li class="rank"><span class="pos">97</span><span class="name bad">(8) gGhhZFlCHP</span><span class="val bad">9.7</span></li>
    <li class="rank"><span class="pos">98</span><span class="name bad">(9) emavLKfhzN</span><span class="val bad">9.8</span></li>
    <li class="rank"><span class="pos">99</span><span class="name bad">(7) PyuviZHBxH</span><span class="val bad">9.8</span></li>
    <li class="rank"><span class="pos">100</span><span class="name bad">(5) LIdsyctcWm</span><span class="val bad">9.9</span></li>
  </ol>
</section>

</main>
</body>
</html>
```